GlowRA (Beer/Wine candles) Edgy Candle with a Cause

Help us to help others. GlowRa is a beautifully scented natural soy candle made using repurposed beer/ wine bottles while at the same time donating a portion of our profits to youth alcohol education programs. (1. Waste = Repurposed beer/wine bottle, 2.) glowRA = (anti) drunk/alcohol 3.) Ed = education/prevention programs.)
We're looking for a design that is cool and bold yet elegant and appeals to women (90% of our customers.) No traditional beer label designs please.

The "GlowRA" logo should appear prominently in the design with the scent name (in a different font) "on top." (See the "Chocolate Glowra" poster attached.

Examples of actual scents: Amber Drift, Velvet Sunrise, Frosted Mintleaf. (None of the fragrances smell like beer/alcohol or wine.)

Also the ED in GlowRRA should stand out in some way.

The emphasis should not be on the recycling aspect, so no obvious recycling symbols.

We are open to different interpretations and have attached varying examples that we like.
Note: a "blackboard/chalkboard" label is an idea since this deals with education.

Note: files & fonts used in the final design should be editable so that we can add other scent names as needed.

Target Market(s)

Candle buyers, specifically women between the ages of 16-45

Requirements
Must have
• 1.)Free fonts or license fonts under $20.00 2.) fonts modified to look unique/original. 3.) Editable Scent name 4.) Burning instructions 5.) Warning Info
• Burning Instructions: Trim wick to 1/4" before each lighting. Keep free from foreign materials including wick trimmings. For an even burn, burn for at least 1 hour but not more than 4 hours at a time. Discontinue use when 1/4" of wax remains. Discard or recycle after use.
• Warning: Burn candle within sight. Keep out of reach of children and pets. Keep away from things that catch fire. Use with caution.
Nice to have
• Colored Scent Names
Should not have
• recycle symbols

```html
<!DOCTYPE html>
<html lang="en">
<head>
<meta charset="utf-8">
<title>GlowRA – Amber Drift label options</title>
<link rel="stylesheet" href="https://fonts.googleapis.com/css2?family=Caveat:wght@500&family=Cinzel:wght@700&family=Patrick+Hand&display=swap">
<style>
  :root {
    --backdrop: #9a5a1c;
    --board: #262626;
    --board-edge: #1c1c1c;
    --chalk: #f4f4f0;
    --chalk-soft: #d9d9d4;
    --sky: #a9def0;
    --butter: #e8c13a;
    --blush: #e7b2c6;
    --caption: #fbf1e2;
  }
  * { margin: 0; padding: 0; box-sizing: border-box; }
  html, body { width: 1200px; height: 907px; overflow: hidden; }
  body { background: var(--backdrop); position: relative; font-family: "Patrick Hand", cursive; }

  .label {
    position: absolute;
    width: 520px;
    height: 676px;
    background: radial-gradient(ellipse at 50% 45%, #303030 0%, var(--board) 60%, var(--board-edge) 100%);
    box-shadow: 0 4px 14px rgba(0,0,0,.45);
  }
  .label--one { left: 68px; top: 97px; }
  .label--two { left: 634px; top: 99px; }

  .label__lines { position: absolute; inset: 0; }

  .scent-name {
    position: absolute; left: 82px; top: 100px; width: 360px;
    text-align: center; font-family: "Caveat", cursive; font-weight: 500;
    font-size: 60px; line-height: 1; white-space: nowrap;
  }
  .scent-name__first { color: var(--sky); }
  .scent-name__second { color: var(--butter); }

  .brand-name {
    position: absolute; left: 10px; top: 180px; width: 500px;
    text-align: center; font-family: "Patrick Hand", cursive; font-weight: 400;
    line-height: 1; color: var(--chalk); white-space: nowrap;
  }
  .brand-name__root { font-size: 132px; }
  .brand-name__accent { font-size: 176px; letter-spacing: 2px; }

  .product-notes {
    position: absolute; left: 140px; top: 384px;
    font-family: "Caveat", cursive; font-weight: 500;
    font-size: 31px; line-height: 34px; color: var(--blush);
  }

  .bottle-note {
    position: absolute; left: 322px; top: 398px; width: 150px;
    text-align: center; font-size: 23px; line-height: 27px; color: var(--chalk);
  }

  .measure {
    position: absolute; font-size: 22px; line-height: 1; color: var(--chalk);
    text-align: center;
  }
  .measure--volume { left: 54px; top: 580px; width: 82px; transform: rotate(-6deg); }
  .measure--strength { left: 134px; top: 590px; width: 88px; font-size: 20px; }

  .heart, .candles { position: absolute; }
  .heart { border-radius: 45% 45% 50% 50%; }
  .heart--top { left: 436px; top: 86px; width: 26px; height: 24px; background: var(--chalk-soft); opacity: .7; }
  .heart--sky { left: 52px; top: 160px; width: 30px; height: 28px; background: var(--sky); opacity: .8; }
  .heart--rose { left: 90px; top: 192px; width: 26px; height: 24px; background: var(--blush); opacity: .7; }
  .heart--gold { left: 446px; top: 344px; width: 28px; height: 26px; background: var(--butter); opacity: .75; }
  .heart--pink { left: 104px; top: 476px; width: 24px; height: 22px; background: var(--blush); opacity: .9; }
  .candles {
    left: 302px; top: 478px; width: 120px; height: 140px;
    background: linear-gradient(180deg, rgba(240,240,236,.06), rgba(240,240,236,.2));
    border-radius: 8px;
  }

  .caption {
    position: absolute; top: 790px; width: 300px;
    text-align: center; font-family: "Cinzel", serif; font-weight: 700;
    font-size: 38px; color: var(--caption); letter-spacing: 1px;
  }
  .caption--one { left: 161px; }
  .caption--two { left: 744px; }
</style>
</head>
<body>

<section class="label label--one">
  <svg class="label__lines" width="520" height="676" viewBox="0 0 520 676" fill="none" stroke="#f2f2ee" stroke-width="3" stroke-linecap="round">
    <ellipse cx="262" cy="136" rx="180" ry="52"/>
    <path d="M230 66 Q360 60 430 80 Q475 110 470 200"/>
    <path d="M456 186 L470 202 L482 184"/>
    <path d="M104 354 Q190 340 262 328"/>
    <path d="M138 448 Q88 430 84 362"/>
    <path d="M72 374 L84 358 L96 374"/>
    <ellipse cx="397" cy="426" rx="92" ry="46"/>
    <rect x="52" y="574" width="86" height="38" transform="rotate(-6 95 593)"/>
    <rect x="134" y="586" width="90" height="32"/>
  </svg>
  <div class="heart heart--top" role="img" aria-label="Small chalk heart outline"></div>
  <div class="heart heart--sky" role="img" aria-label="Light blue chalk heart"></div>
  <div class="heart heart--rose" role="img" aria-label="Pink chalk heart"></div>
  <div class="heart heart--gold" role="img" aria-label="Yellow chalk heart"></div>
  <div class="heart heart--pink" role="img" aria-label="Filled pink chalk heart"></div>
  <p class="scent-name"><span class="scent-name__first">Amber</span> <span class="scent-name__second">Drift</span></p>
  <h1 class="brand-name"><span class="brand-name__root">Glow</span><span class="brand-name__accent">RA</span></h1>
  <p class="product-notes">premium<br>scented<br>natural<br>soy wax</p>
  <p class="bottle-note">Repurposed<br>wine bottles</p>
  <div class="candles" role="img" aria-label="Chalk drawing of two lit candles in glass jars with rising smoke"></div>
  <p class="measure measure--volume">70 ml</p>
  <p class="measure measure--strength">40% Vol</p>
</section>

<section class="label label--two">
  <svg class="label__lines" width="520" height="676" viewBox="0 0 520 676" fill="none" stroke="#f2f2ee" stroke-width="3" stroke-linecap="round">
    <ellipse cx="262" cy="136" rx="180" ry="52"/>
    <path d="M230 66 Q360 60 430 80 Q475 110 470 200"/>
    <path d="M456 186 L470 202 L482 184"/>
    <path d="M96 352 Q200 344 270 338"/>
    <path d="M138 448 Q88 430 84 362"/>
    <path d="M72 374 L84 358 L96 374"/>
    <ellipse cx="397" cy="426" rx="92" ry="46"/>
    <rect x="52" y="574" width="86" height="38" transform="rotate(-6 95 593)"/>
    <rect x="134" y="586" width="90" height="32"/>
  </svg>
  <div class="heart heart--top" role="img" aria-label="Small chalk heart outline"></div>
  <div class="heart heart--sky" role="img" aria-label="Light blue chalk heart"></div>
  <div class="heart heart--rose" role="img" aria-label="Pink chalk heart"></div>
  <div class="heart heart--gold" role="img" aria-label="Yellow chalk heart"></div>
  <div class="heart heart--pink" role="img" aria-label="Filled pink chalk heart"></div>
  <p class="scent-name"><span class="scent-name__first">Amber</span> <span class="scent-name__second">Drift</span></p>
  <h2 class="brand-name"><span class="brand-name__root">glow</span><span class="brand-name__accent">RA</span></h2>
  <p class="product-notes">premium<br>scented<br>natural<br>soy wax</p>
  <p class="bottle-note">Repurposed<br>wine bottles</p>
  <div class="candles" role="img" aria-label="Chalk drawing of two lit candles in glass jars with rising smoke"></div>
  <p class="measure measure--volume">70 ml</p>
  <p class="measure measure--strength">40% Vol</p>
</section>

<p class="caption caption--one">Option 1</p>
<p class="caption caption--two">Option 2</p>

</body>
</html>
```